Hong Kong residential leasing and sales company needs a website design

Hong Kong has many competitive real estate agents. The majority of us have the same listings so, besides the team and experience, a website is what makes us stand out. A first impression. We need our website to be user friendly, informative and to have a wow factor. Most sites are generic so whilst we are close to accepting that maybe that's the only formula which works....we would like to see if we're missing something! Our clients are a mix of International users of all ages but probably ultimately 35+.. We have a logo (attached) which we would like to keep - designed by artmarketly. Flexible with colours except red.
examples of our competitors are:
http://www.brindlewoodestates.example
http://www.nuvo.example/home
http://www.premierdwellingsvx.example
http://www.orchid-lettings.example
http://www.tidemark-harrowgates.example
We were thinking of having the following in a menu bar with drop downs for most...some more than others. Home / For Sale / For Rent / Property 101 / About us / Contact Us ..
Look forward to seeing your ideas. Thanks in advance.

```html
<!DOCTYPE html>
<html lang="en">
<head>
<meta charset="utf-8">
<title>Harbourline Homes</title>
<link href="https://fonts.googleapis.com/css2?family=PT+Serif:wght@400;700&display=swap" rel="stylesheet">
<style>
:root{
  --purple:#6b3d8e;
  --purple-dark:#4f2a6d;
  --purple-soft:rgba(107,61,142,.88);
  --charcoal:#3a3a3a;
  --nav:#4a4a4a;
  --ink:#333;
  --muted:#777;
  --band:#e9e9e9;
  --page:#f6f6f6;
  --white:#fff;
}
*{box-sizing:border-box;margin:0;padding:0}
html,body{width:1200px;height:2348px;overflow:hidden}
body{background:var(--page);font-family:"PT Serif",Georgia,serif;color:var(--ink);position:relative}
.wrap{width:1056px;margin:0 auto;position:relative}

/* header */
.site-header{height:152px;background:var(--white);position:relative}
.language-tab{position:absolute;right:72px;top:0;background:var(--purple);color:var(--white);font-size:15px;padding:4px 14px;border-radius:0 0 4px 4px}
.brand{position:absolute;left:50%;top:40px;transform:translateX(-50%);display:flex;flex-direction:column;align-items:center;gap:8px}
.brand-square{width:56px;height:56px;background:var(--purple)}
.brand-name{font-size:26px;font-weight:700;color:var(--purple);letter-spacing:4px;white-space:nowrap}
.contact-box{position:absolute;right:72px;top:44px;text-align:right}
.call-label{font-size:14px;color:var(--muted);letter-spacing:1px}
.call-number{font-size:24px;color:var(--purple);font-weight:700}
.social-row{display:flex;gap:8px;justify-content:flex-end;margin-top:8px}
.social-row span{width:24px;height:24px;border-radius:50%;background:var(--purple)}

/* nav */
.main-nav{height:40px;background:var(--nav);border-top:3px solid var(--purple)}
.main-nav .wrap{display:flex;align-items:center;height:100%}
.main-nav a{color:var(--white);text-decoration:none;font-size:15px;padding:0 26px;line-height:37px;border-right:1px solid #5c5c5c}
.main-nav a.active{background:#2e2e2e}
.search{margin-left:auto;width:190px;height:24px;background:var(--white);border-radius:3px;position:relative}
.search svg{position:absolute;right:6px;top:4px}

/* hero */
.hero{height:548px;position:relative;background:linear-gradient(180deg,#6d5e52 0%,#a4917d 35%,#d8cbb8 60%,#8a7460 100%)}
.welcome{position:absolute;left:260px;width:680px;bottom:0;height:140px;background:var(--purple-soft);color:var(--white);text-align:center;padding:16px 40px}
.welcome h1{font-size:24px;font-weight:700;letter-spacing:2px;margin-bottom:10px}
.welcome p{font-size:14px;line-height:1.45}
.welcome a{color:var(--white);font-weight:700}

/* section headings */
.section-title{font-size:20px;font-weight:700;color:var(--charcoal);letter-spacing:1px;border-bottom:1px solid #ccc;padding-bottom:8px}

/* for sale */
.for-sale{padding-top:20px;height:352px}
.listing-grid{display:grid;grid-template-columns:repeat(4,1fr);gap:16px;margin-top:16px}
.listing-photo{height:128px}
.listing-name{background:var(--white);font-size:13px;font-weight:700;padding:10px 12px;color:var(--charcoal);border:1px solid #ddd;border-top:0}
.btn-row{display:flex;justify-content:center;gap:14px;margin-top:28px}
.btn{display:inline-block;font-size:13px;color:var(--white);padding:9px 22px;letter-spacing:1px;text-decoration:none}
.btn-purple{background:var(--purple)}
.btn-dark{background:var(--charcoal)}

/* news */
.latest-news{background:var(--band);height:440px;padding-top:24px;border-top:1px solid #ddd;border-bottom:1px solid #ddd}
.news-grid{display:grid;grid-template-columns:repeat(4,1fr);gap:16px;margin-top:16px}
.news-card{background:var(--white);border:1px solid #ddd}
.news-photo{height:136px}
.news-body{padding:10px 12px}
.news-body h3{font-size:13px;color:var(--purple);margin-bottom:6px}
.news-body p{font-size:12px;color:var(--muted);line-height:1.4;margin-bottom:8px}
.read-more{display:inline-block;background:var(--charcoal);color:var(--white);font-size:11px;padding:4px 10px}
.latest-news .btn-row{margin-top:36px}

/* agents */
.agents{padding-top:40px;height:440px}
.agents-intro{text-align:center;font-size:14px;color:var(--muted);line-height:1.5;width:760px;margin:20px auto 0}
.agent-row{display:flex;justify-content:center;gap:62px;margin-top:44px}
.agent{text-align:center;width:120px}
.agent-photo{width:108px;height:108px;border-radius:50%;margin:0 auto;border:4px solid var(--white);box-shadow:0 0 0 1px #ccc}
.agent-name{font-size:13px;margin-top:12px;color:var(--charcoal)}
.agents .btn-row{margin-top:34px}

/* footer */
.site-footer{position:absolute;left:0;top:2040px;width:1200px;height:260px;background:var(--purple);color:var(--white)}
.footer-cols{display:grid;grid-template-columns:230px 230px 230px 1fr;padding-top:32px}
.footer-cols h4{font-size:15px;letter-spacing:1px;margin-bottom:12px}
.footer-cols ul{list-style:none;font-size:13px;line-height:1.85}
.footer-cols li::before{content:"» ";opacity:.8}
.follow li{display:flex;align-items:center;gap:10px;line-height:1;margin-bottom:10px}
.follow li::before{content:none}
.follow span{width:22px;height:22px;border-radius:50%;background:var(--white);opacity:.9}
.about-block{display:flex;gap:14px}
.about-logo{flex:0 0 120px;height:100px;background:var(--white);display:flex;flex-direction:column;align-items:center;justify-content:center;gap:6px;padding:0 6px;text-align:center}
.about-logo i{width:28px;height:28px;background:var(--purple)}
.about-logo b{font-size:11px;line-height:1.25;color:var(--purple);letter-spacing:.5px}
.about-block p{font-size:12px;line-height:1.45;margin-bottom:8px}
.copyright{position:absolute;left:0;top:2300px;width:1200px;height:48px;background:var(--purple-dark);color:#ddd;font-size:12px}
.copyright .wrap{line-height:48px}
</style>
</head>
<body>

<header class="site-header">
  <div class="language-tab">Language ✕</div>
  <div class="brand">
    <div class="brand-square"></div>
    <div class="brand-name">HARBOURLINE HOMES</div>
  </div>
  <div class="contact-box">
    <div class="call-label">CALL NOW</div>
    <div class="call-number">02-8470-3916</div>
    <div class="social-row"><span></span><span></span><span></span><span></span></div>
  </div>
</header>

<nav class="main-nav">
  <div class="wrap">
    <a class="active">HOME</a><a>FOR SALE</a><a>FOR RENT</a><a>PROPERTY 101</a><a>ABOUT US</a><a>CONTACT US</a>
    <div class="search">
      <svg width="16" height="16" viewBox="0 0 16 16"><circle cx="6.5" cy="6.5" r="4.5" fill="none" stroke="#555" stroke-width="2"/><line x1="10" y1="10" x2="14" y2="14" stroke="#555" stroke-width="2"/></svg>
    </div>
  </div>
</nav>

<section class="hero" role="img" aria-label="Modern apartment living room with sofa, armchairs and city view windows">
  <div class="welcome">
    <h1>WELCOME TO HARBOURLINE HOMES</h1>
    <p>Lorem ipsum dolor sit amet, consectetur adipiscing elit. Maecenas lectus leo, dapibus nec molestie adipiscing ullamcorper massa eu. Consectetur adipiscing elit dapibus imperdiet magna eu, consectetur adipiscing elit. Maecenas lectus leo. <a>Read more »</a></p>
  </div>
</section>

<section class="for-sale">
  <div class="wrap">
    <h2 class="section-title">FOR SALE</h2>
    <div class="listing-grid">
      <div><div class="listing-photo" role="img" aria-label="Villa with pool" style="background:linear-gradient(180deg,#9cc3e0,#d9cfb8 60%,#6d8f5a)"></div><div class="listing-name">PROPERTY NAME HERE</div></div>
      <div><div class="listing-photo" role="img" aria-label="House exterior with lawn" style="background:linear-gradient(180deg,#b8d3ea,#e8e2d2 55%,#7c9a5e)"></div><div class="listing-name">PROPERTY NAME HERE</div></div>
      <div><div class="listing-photo" role="img" aria-label="Bright kitchen interior" style="background:linear-gradient(180deg,#f0ece4,#cfc6b6 60%,#8b7d6c)"></div><div class="listing-name">PROPERTY NAME HERE</div></div>
      <div><div class="listing-photo" role="img" aria-label="Modern house lit at dusk" style="background:linear-gradient(180deg,#2d4a78,#6e86b0 45%,#e0b26a 70%,#3c3a3a)"></div><div class="listing-name">PROPERTY NAME HERE</div></div>
    </div>
    <div class="btn-row">
      <a class="btn btn-purple">VIEW FOR RENT PROPERTIES</a>
      <a class="btn btn-dark">VIEW FOR SALE PROPERTIES</a>
    </div>
  </div>
</section>

<section class="latest-news">
  <div class="wrap">
    <h2 class="section-title">LATEST NEWS</h2>
    <div class="news-grid">
      <article class="news-card"><div class="news-photo" role="img" aria-label="Glass office towers" style="background:linear-gradient(160deg,#3f6ea8,#a9c6e3 60%,#2b4f7d)"></div><div class="news-body"><h3>ARTICLE TITLE GOES HERE</h3><p>Lorem ipsum dolor sit amet, consectetur elit. Vestibulum donec ipsum.</p><span class="read-more">Read more</span></div></article>
      <article class="news-card"><div class="news-photo" role="img" aria-label="Business team in an office" style="background:linear-gradient(180deg,#dfe3e8,#9aa5b3 60%,#4d5866)"></div><div class="news-body"><h3>ARTICLE TITLE GOES HERE</h3><p>Lorem ipsum dolor sit amet, consectetur elit. Vestibulum donec ipsum.</p><span class="read-more">Read more</span></div></article>
      <article class="news-card"><div class="news-photo" role="img" aria-label="City skyline at dusk" style="background:linear-gradient(180deg,#2a3f7a,#5d78b8 50%,#d89a5a 80%,#2a2a3a)"></div><div class="news-body"><h3>ARTICLE TITLE GOES HERE</h3><p>Lorem ipsum dolor sit amet, consectetur elit. Vestibulum donec ipsum.</p><span class="read-more">Read more</span></div></article>
      <article class="news-card"><div class="news-photo" role="img" aria-label="Agent meeting clients" style="background:linear-gradient(180deg,#eef0f2,#b7bcc2 60%,#6b7078)"></div><div class="news-body"><h3>ARTICLE TITLE GOES HERE</h3><p>Lorem ipsum dolor sit amet, consectetur elit. Vestibulum donec ipsum.</p><span class="read-more">Read more</span></div></article>
    </div>
    <div class="btn-row"><a class="btn btn-purple">VIEW LATEST ARTICLES</a></div>
  </div>
</section>

<section class="agents">
  <div class="wrap">
    <h2 class="section-title">FEATURURED AGENTS</h2>
    <p class="agents-intro">Lorem ipsum dolor sit amet, consectetur adipiscing elit. Maecenas lectus leo, dapibus nec imperdiet magna eu, consectetur adipiscing elit. Dapibus imperdiet magna consectetur adipiscing elit magna.</p>
    <div class="agent-row">
      <div class="agent"><div class="agent-photo" role="img" aria-label="Agent portrait" style="background:linear-gradient(180deg,#d8d8d8,#7a7a7a)"></div><div class="agent-name">Agent Name Here</div></div>
      <div class="agent"><div class="agent-photo" role="img" aria-label="Agent portrait" style="background:linear-gradient(180deg,#e2d7cc,#5a4a44)"></div><div class="agent-name">Agent Name Here</div></div>
      <div class="agent"><div class="agent-photo" role="img" aria-label="Agent portrait" style="background:linear-gradient(180deg,#e4e4e4,#3c3c44)"></div><div class="agent-name">Agent Name Here</div></div>
      <div class="agent"><div class="agent-photo" role="img" aria-label="Agent portrait" style="background:linear-gradient(180deg,#e6dcd2,#4a3c36)"></div><div class="agent-name">Agent Name Here</div></div>
      <div class="agent"><div class="agent-photo" role="img" aria-label="Agent portrait" style="background:linear-gradient(180deg,#ece2d8,#2e2a2a)"></div><div class="agent-name">Agent Name Here</div></div>
    </div>
    <div class="btn-row"><a class="btn btn-purple">VIEW LIST OF OUR AGENTS</a></div>
  </div>
</section>

<footer class="site-footer">
  <div class="wrap footer-cols">
    <div><h4>QUICKLINKS</h4><ul><li>Home</li><li>For Sale</li><li>For Rent</li><li>Property 101</li><li>Contact us</li></ul></div>
    <div><h4>USEFUL INFO</h4><ul><li>FAQ</li><li>Sitemap</li><li>Terms &amp; Agreements</li><li>Agents</li><li>Privacy Policy</li></ul></div>
    <div class="follow"><h4>FOLLOW US</h4><ul><li><span></span>Chirpline</li><li><span></span>Friendbook</li><li><span></span>Snapgrid</li><li><span></span>Rss Feed</li></ul></div>
    <div><h4>ABOUT US</h4>
      <div class="about-block">
        <div class="about-logo"><i></i><b>HARBOURLINE<br>HOMES</b></div>
        <div><p>Lorem ipsum dolor sit amet, consectetur adipiscing elit. Maecenas lectus leo dapibus nec.</p><p>Nam molestie magna eu massa dapibus nec adipiscing elit imperdiet.</p></div>
      </div>
    </div>
  </div>
</footer>
<div class="copyright"><div class="wrap">Copyright © 2014 Harbourline Homes. All right reserved</div></div>

</body>
</html>
```